Increased budget: GUI redesign: 10 year old user interface needs modern look-and-feel

UPDATE: Please DO look at more than only th eone image I attached! Almost all designs are simply reworks of that one picture. That is not what we are looking for. Check out the video to understand what the product does, and try to make something better.
We have an existing app (see https://www.vextorane.com/downloadBrivoPanel.php?vers=3_9_1_140964&dir=Vextorane_OEM/3_9_1_140964&name=DSP_Control_Software) which needs refreshing. See also a video here: https://vextorane-oem.com/software/ and the user manual attached here. The GUI is now 800x400 pixels, which is too small; and not scalable, which will be fixed in the future. We need a new, modern look-and-feel, and images that can be exported from the design in various sizes. The current design is attached as well as a collection of PNG files. The overall layout can stay similar, although we are open to good ideas for improvements. The design should be targeted at professional users, not end users; the product is used by audio professionals (e.g. sound engineers, loudspeaker designers). Also see our web version: https://www.vextorane.com/brivopanel/skins/1_1_2/container.html?MAC=Demo%201x2
The winner will also be asked to do a full design of the application GUI (based on the design done here), with several more windows etc, and additional payment depending on the work to be done.

Target Market(s)

Professional audio

Industry/Entity Type

Audio / Industrial

Font styles to use
Other font styles liked:
• Futura (not mandatory)

Colors

Designer to choose colors to be used in the design.

Requirements
Must have
• Modern, timeless design, not too bling bling
Nice to have
• Flat design
Should not have
• 3D, bling bling, many colours, etc

```html
<!DOCTYPE html>
<html lang="en">
<head>
<meta charset="utf-8">
<title>Oltrane Control – GUI Redesign</title>
<link href="https://fonts.googleapis.com/css2?family=DM+Sans:wght@400;500;700&display=swap" rel="stylesheet">
<style>
  :root{
    --page:#1b2232;
    --frame:#2b3447;
    --sidebar:#182136;
    --main:#0e1629;
    --footer:#0b1223;
    --btn:#242f4a;
    --btn-line:#3a4664;
    --field:#1c2640;
    --purple:#7a5ce8;
    --purple-dot:#8d74f0;
    --handle:#e4e2f0;
    --text:#e6e9f2;
    --muted:#7c86a0;
    --dim:#4a5570;
    --headline:#5d6779;
    --caption:#3b4558;
    --track:#2e3850;
    --tick:#56607a;
    --green:#5ad13d;
    --red:#e0352b;
  }
  *{margin:0;padding:0;box-sizing:border-box}
  html,body{width:1200px;height:1017px;overflow:hidden;background:var(--page)}
  body{position:relative;font-family:"DM Sans",sans-serif}
  .caption{position:absolute;left:78px;font-size:18px;font-weight:500;color:var(--caption)}
  .caption--original{top:77px}
  .caption--max{top:346px}
  .hero{position:absolute;left:526px;top:138px}
  .hero__title{font-size:54px;font-weight:700;color:var(--headline);letter-spacing:-.5px;line-height:1}
  .hero__sub{margin-top:18px;font-size:21px;font-weight:500;color:var(--caption)}
  .stage{position:absolute;left:0;top:0;width:1200px;height:1017px}
  .t-label{font-family:"DM Sans",sans-serif;font-size:17px;font-weight:500;fill:var(--text)}
  .t-btn{font-family:"DM Sans",sans-serif;font-size:18px;fill:var(--text);text-anchor:middle}
  .t-field{font-family:"DM Sans",sans-serif;font-size:18px;fill:var(--muted);text-anchor:middle}
  .t-title{font-family:"DM Sans",sans-serif;font-size:27px;font-weight:700;fill:#4d5874;text-anchor:middle}
  .t-scale{font-family:"DM Sans",sans-serif;font-size:12px;fill:var(--muted);text-anchor:end}
  .t-row{font-family:"DM Sans",sans-serif;font-size:18px;fill:var(--muted)}
  .t-value{font-family:"DM Sans",sans-serif;font-size:18px;fill:var(--muted);text-anchor:middle}
  .t-chan{font-family:"DM Sans",sans-serif;font-size:16px;fill:var(--muted);text-anchor:middle}
  .t-tab{font-family:"DM Sans",sans-serif;font-size:19px;font-weight:500;text-anchor:middle}
</style>
</head>
<body>

<p class="caption caption--original">Original Version 800x400</p>
<div class="hero">
  <h1 class="hero__title">GUI Redesign</h1>
  <p class="hero__sub">Thank you for watching my works</p>
</div>
<p class="caption caption--max">Max Version</p>

<svg class="stage" width="1200" height="1017" viewBox="0 0 1200 1017" xmlns="http://www.w3.org/2000/svg">
  <defs>
    <pattern id="ticks" width="12" height="4.4" patternUnits="userSpaceOnUse">
      <rect x="0" y="0" width="12" height="1" fill="var(--tick)"/>
    </pattern>
    <pattern id="ticks-major" width="12" height="22" patternUnits="userSpaceOnUse">
      <rect x="-2" y="0" width="16" height="1.5" fill="#7a849c"/>
    </pattern>

    <g id="ladder">
      <rect x="-6" y="124" width="12" height="446" fill="url(#ticks)"/>
      <rect x="-8" y="124" width="16" height="446" fill="url(#ticks-major)"/>
    </g>

    <g id="handle">
      <rect x="-10" y="-21" width="20" height="42" rx="3" fill="var(--handle)"/>
      <g stroke="var(--purple)" stroke-width="1.6">
        <line x1="-6" y1="-13" x2="6" y2="-13"/><line x1="-6" y1="-9" x2="6" y2="-9"/>
        <line x1="-6" y1="-5" x2="6" y2="-5"/><line x1="-6" y1="-1" x2="6" y2="-1"/>
        <line x1="-6" y1="3" x2="6" y2="3"/><line x1="-6" y1="7" x2="6" y2="7"/>
        <line x1="-6" y1="11" x2="6" y2="11"/><line x1="-6" y1="15" x2="6" y2="15"/>
      </g>
    </g>

    <g id="track">
      <rect x="-9" y="120" width="18" height="454" rx="9" fill="none" stroke="var(--track)" stroke-width="3"/>
    </g>

    <g id="dot">
      <circle r="9" fill="var(--purple)"/>
      <circle r="3" fill="#e8e4ff"/>
    </g>

    <symbol id="gui" viewBox="0 0 1762 890">
      <!-- panel body -->
      <rect width="1762" height="890" rx="40" fill="var(--main)"/>
      <path d="M40 0H322V805H0V40A40 40 0 0 1 40 0Z" fill="var(--sidebar)"/>
      <path d="M0 805H1762V850A40 40 0 0 1 1722 890H40A40 40 0 0 1 0 850Z" fill="var(--footer)"/>

      <!-- sidebar -->
      <g class="sidebar">
        <text class="t-label" x="31" y="63">Local Presets</text>
        <rect x="31" y="85" width="121" height="34" fill="var(--btn)" stroke="var(--btn-line)"/>
        <text class="t-btn" x="91.5" y="109">Store</text>
        <rect x="170" y="85" width="121" height="34" fill="var(--btn)" stroke="var(--btn-line)"/>
        <text class="t-btn" x="230.5" y="109">Load</text>

        <text class="t-label" x="31" y="173">Unit Presets</text>
        <rect x="31" y="193" width="260" height="39" fill="var(--field)" stroke="var(--btn-line)"/>
        <text class="t-field" x="161" y="218">No Name</text>
        <rect x="31" y="246" width="260" height="44" fill="var(--btn)" stroke="var(--btn-line)"/>
        <text class="t-btn" x="150" y="274">1: Empty Preset</text>
        <path d="M264 262l9 5-9 5z" fill="var(--purple-dot)"/>
        <rect x="31" y="306" width="121" height="34" fill="var(--btn)" stroke="var(--btn-line)"/>
        <text class="t-btn" x="91.5" y="330">Store</text>
        <rect x="170" y="306" width="121" height="34" fill="var(--btn)" stroke="var(--btn-line)"/>
        <text class="t-btn" x="230.5" y="330">Load</text>

        <text class="t-label" x="31" y="382">Link</text>
        <rect x="274" y="369" width="16" height="11" rx="1" fill="var(--green)"/>
        <rect x="31" y="400" width="260" height="43" fill="var(--btn)" stroke="var(--btn-line)"/>
        <text class="t-btn" x="132" y="428">VXP428</text>
        <path d="M264 417l9 5-9 5z" fill="var(--purple-dot)"/>

        <text class="t-label" x="31" y="497">Unit Name</text>
        <rect x="31" y="514" width="260" height="44" fill="var(--field)" stroke="var(--btn-line)"/>
        <text class="t-field" x="161" y="542">VXP428</text>

        <text class="t-label" x="31" y="611">Status</text>
        <rect x="274" y="599" width="16" height="11" rx="1" fill="var(--red)"/>
        <rect x="31" y="629" width="260" height="44" fill="var(--btn)" stroke="var(--btn-line)"/>
        <text class="t-btn" x="161" y="657">Details</text>
      </g>

      <!-- header -->
      <text class="t-title" x="882" y="54">Oltrane Control DSP Commend Centre</text>
      <g class="header-icons">
        <circle cx="1662" cy="45" r="14" fill="var(--btn)" stroke="var(--btn-line)"/>
        <circle cx="1662" cy="45" r="5.5" fill="none" stroke="var(--text)" stroke-width="1.8"/>
        <circle cx="1662" cy="45" r="2" fill="var(--text)"/>
        <circle cx="1706" cy="45" r="14" fill="var(--btn)" stroke="var(--btn-line)"/>
        <path d="M1701 40l10 10M1711 40l-10 10" stroke="var(--text)" stroke-width="2" stroke-linecap="round"/>
      </g>

      <!-- dB scales -->
      <g class="scale-left">
        <text class="t-scale" x="417" y="130">+12</text><text class="t-scale" x="417" y="174">+6</text>
        <text class="t-scale" x="417" y="218">0</text><text class="t-scale" x="417" y="262">-6</text>
        <text class="t-scale" x="417" y="306">-12</text><text class="t-scale" x="417" y="350">-18</text>
        <text class="t-scale" x="417" y="394">-24</text><text class="t-scale" x="417" y="438">-30</text>
        <text class="t-scale" x="417" y="482">-36</text><text class="t-scale" x="417" y="526">-42</text>
        <text class="t-scale" x="417" y="570">-48</text>
      </g>
      <g class="scale-right">
        <text class="t-scale" x="1688" y="128">+12</text><text class="t-scale" x="1688" y="172">+6</text>
        <text class="t-scale" x="1688" y="216">0</text><text class="t-scale" x="1688" y="260">-6</text>
        <text class="t-scale" x="1688" y="304">-12</text><text class="t-scale" x="1688" y="348">-18</text>
        <text class="t-scale" x="1688" y="392">-24</text><text class="t-scale" x="1688" y="436">-30</text>
        <text class="t-scale" x="1688" y="480">-36</text><text class="t-scale" x="1688" y="524">-42</text>
        <text class="t-scale" x="1688" y="568">-48</text>
        <use href="#ladder" x="1711" y="0"/>
      </g>

      <!-- faders: inputs -->
      <g class="faders-in">
        <use href="#ladder" x="438"/><use href="#track" x="472"/>
        <rect x="468" y="251" width="8" height="317" rx="4" fill="var(--purple)"/><use href="#handle" x="472" y="251"/>
        <use href="#ladder" x="530"/><use href="#track" x="564"/>
        <rect x="560" y="372" width="8" height="196" rx="4" fill="var(--purple)"/><use href="#handle" x="564" y="372"/>
        <use href="#ladder" x="626"/><use href="#track" x="660"/>
        <rect x="656" y="255" width="8" height="313" rx="4" fill="var(--purple)"/><use href="#handle" x="660" y="255"/>
        <use href="#ladder" x="720"/><use href="#track" x="754"/>
        <rect x="750" y="165" width="8" height="403" rx="4" fill="var(--purple)"/><use href="#handle" x="754" y="165"/>
      </g>

      <!-- faders: outputs -->
      <g class="faders-out">
        <use href="#ladder" x="908"/><use href="#track" x="942"/>
        <rect x="938" y="399" width="8" height="169" rx="4" fill="var(--purple)"/><use href="#handle" x="942" y="399"/>
        <use href="#ladder" x="1002"/><use href="#track" x="1036"/>
        <rect x="1032" y="262" width="8" height="306" rx="4" fill="var(--purple)"/><use href="#handle" x="1036" y="262"/>
        <use href="#ladder" x="1096"/><use href="#track" x="1130"/>
        <rect x="1126" y="502" width="8" height="66" rx="4" fill="var(--purple)"/><use href="#handle" x="1130" y="502"/>
        <use href="#ladder" x="1190"/><use href="#track" x="1224"/>
        <rect x="1220" y="195" width="8" height="373" rx="4" fill="var(--purple)"/><use href="#handle" x="1224" y="195"/>
        <use href="#ladder" x="1284"/><use href="#track" x="1318"/>
        <rect x="1314" y="306" width="8" height="262" rx="4" fill="var(--purple)"/><use href="#handle" x="1318" y="306"/>
        <use href="#ladder" x="1378"/><use href="#track" x="1412"/>
        <rect x="1408" y="235" width="8" height="333" rx="4" fill="var(--purple)"/><use href="#handle" x="1412" y="235"/>
        <use href="#ladder" x="1472"/><use href="#track" x="1506"/>
        <rect x="1502" y="289" width="8" height="279" rx="4" fill="var(--purple)"/><use href="#handle" x="1506" y="289"/>
        <use href="#ladder" x="1568"/><use href="#track" x="1602"/>
        <rect x="1598" y="367" width="8" height="201" rx="4" fill="var(--purple)"/><use href="#handle" x="1602" y="367"/>
      </g>

      <!-- link row -->
      <g class="link-row">
        <text class="t-row" x="348" y="644">Link</text>
        <line x1="393" y1="638" x2="1620" y2="638" stroke="var(--track)"/>
        <use href="#dot" x="451" y="638"/><use href="#dot" x="687" y="638"/>
        <use href="#dot" x="974" y="638"/><use href="#dot" x="1084" y="638"/>
        <use href="#dot" x="1172" y="638"/><use href="#dot" x="1392" y="638"/>
        <use href="#dot" x="1569" y="638"/>
      </g>

      <!-- gain values -->
      <g class="values" fill="var(--field)" stroke="var(--btn-line)">
        <rect x="427" y="673" width="56" height="48"/><rect x="519" y="673" width="56" height="48"/>
        <rect x="614" y="673" width="56" height="48"/><rect x="709" y="673" width="56" height="48"/>
        <rect x="894" y="673" width="60" height="48"/><rect x="989" y="673" width="60" height="48"/>
        <rect x="1084" y="673" width="60" height="48"/><rect x="1176" y="673" width="60" height="48"/>
        <rect x="1271" y="673" width="60" height="48"/><rect x="1368" y="673" width="60" height="48"/>
        <rect x="1467" y="673" width="60" height="48"/><rect x="1560" y="673" width="60" height="48"/>
      </g>
      <g class="value-text">
        <text class="t-value" x="455" y="704">0</text><text class="t-value" x="547" y="704">0</text>
        <text class="t-value" x="642" y="704">0</text><text class="t-value" x="737" y="704">0</text>
        <text class="t-value" x="924" y="704">0</text><text class="t-value" x="1019" y="704">0</text>
        <text class="t-value" x="1114" y="704">0</text><text class="t-value" x="1206" y="704">0</text>
        <text class="t-value" x="1301" y="704">0</text><text class="t-value" x="1398" y="704">0</text>
        <text class="t-value" x="1497" y="704">0</text><text class="t-value" x="1590" y="704">0</text>
      </g>

      <!-- mute row -->
      <g class="mute-row">
        <text class="t-row" x="346" y="770">Mute</text>
        <line x1="393" y1="764" x2="1620" y2="764" stroke="var(--track)"/>
        <use href="#dot" x="452" y="764"/><use href="#dot" x="544" y="764"/>
        <use href="#dot" x="643" y="764"/><use href="#dot" x="742" y="764"/>
        <use href="#dot" x="921" y="764"/><use href="#dot" x="1020" y="764"/>
        <use href="#dot" x="1115" y="764"/><use href="#dot" x="1205" y="764"/>
        <use href="#dot" x="1304" y="764"/><use href="#dot" x="1399" y="764"/>
        <use href="#dot" x="1500" y="764"/><use href="#dot" x="1600" y="764"/>
      </g>

      <!-- footer tabs -->
      <g class="tabs">
        <rect x="24" y="823" width="66" height="47" fill="var(--purple)"/>
        <text class="t-tab" x="57" y="853" fill="#ffffff">Main</text>
        <rect x="101" y="823" width="86" height="47" fill="var(--btn)" stroke="var(--btn-line)"/>
        <text class="t-tab" x="144" y="853" fill="var(--muted)">X-over</text>
      </g>
      <g class="channel-tabs" fill="var(--btn)" stroke="var(--btn-line)">
        <rect x="427" y="823" width="56" height="47"/><rect x="519" y="823" width="56" height="47"/>
        <rect x="614" y="823" width="56" height="47"/><rect x="709" y="823" width="56" height="47"/>
        <rect x="894" y="823" width="60" height="47"/><rect x="989" y="823" width="60" height="47"/>
        <rect x="1084" y="823" width="60" height="47"/><rect x="1176" y="823" width="60" height="47"/>
        <rect x="1271" y="823" width="60" height="47"/><rect x="1368" y="823" width="60" height="47"/>
        <rect x="1467" y="823" width="60" height="47"/><rect x="1560" y="823" width="60" height="47"/>
      </g>
      <g class="channel-labels">
        <text class="t-chan" x="455" y="852">In 1</text><text class="t-chan" x="547" y="852">In 2</text>
        <text class="t-chan" x="642" y="852">In 3</text><text class="t-chan" x="737" y="852">In 4</text>
        <text class="t-chan" x="924" y="852">Out 1</text><text class="t-chan" x="1019" y="852">Out 2</text>
        <text class="t-chan" x="1114" y="852">Out 3</text><text class="t-chan" x="1206" y="852">Out 4</text>
        <text class="t-chan" x="1301" y="852">Out 5</text><text class="t-chan" x="1398" y="852">Out 6</text>
        <text class="t-chan" x="1497" y="852">Out 7</text><text class="t-chan" x="1590" y="852">Out 8</text>
      </g>
    </symbol>
  </defs>

  <!-- compact 800x400 view -->
  <rect class="frame frame--compact" x="78.4" y="118" width="349" height="181" rx="7" fill="var(--frame)"/>
  <use href="#gui" x="83.6" y="122.8" width="339" height="172"/>

  <!-- full-size view -->
  <rect class="frame frame--max" x="78.4" y="385" width="1042.5" height="538.7" rx="22" fill="var(--frame)"/>
  <use href="#gui" x="91.7" y="397.8" width="1016" height="513.2"/>
</svg>

</body>
</html>
```